MCDI Root Beer bottle label design.

We produce homemade root beer the same way since 1965. Family owned and third generation owner. The root beer will bring you back 50 years. This will go on a brown beer bottle. Our website is www.marburycreekdrivein.example. We have a logo on our website but I would like something different. we are a 50's style drive in restaurant like J&P and Vireo. I would like this to be a new logo for our business.

Target Market(s)

All ages

Colors
f37122
ffffff
000000

Requirements
Must have
• Easy to read. Retro style font with a lot of white in the logo. I would like to be able to pull the logo out separately and put that just on the bottle if I choose. I added some examples of labels and the style of font I like.

```html
<!DOCTYPE html>
<html lang="en">
<head>
<meta charset="utf-8">
<title>MCDI Root Beer Label</title>
<link rel="stylesheet" href="https://fonts.googleapis.com/css2?family=Uncial+Antiqua&family=Kaushan+Script&family=Oswald:wght@400;500&family=Patua+One&display=swap">
<style>
  :root {
    --stage: #1c1a19;
    --label: #4a0b07;
    --amber: #f2a033;
    --white: #ffffff;
  }
  html, body {
    margin: 0;
    width: 1200px;
    height: 960px;
    overflow: hidden;
    background: var(--stage);
  }
  .label {
    position: absolute;
    left: 239px;
    top: 30px;
    width: 722px;
    height: 900px;
    display: block;
  }
  .label-bg { fill: var(--label); }
  .frame-line { fill: none; stroke: var(--amber); }
  .amber-fill { fill: var(--amber); }
  .tagline {
    font-family: "Oswald", sans-serif;
    font-weight: 500;
    font-size: 21px;
    letter-spacing: 1px;
    fill: var(--white);
  }
  .brand-name {
    font-family: "Uncial Antiqua", serif;
    fill: var(--white);
  }
  .brand-top { font-size: 74px; }
  .brand-bottom { font-size: 72px; }
  .number-mark {
    font-family: "Oswald", sans-serif;
    font-weight: 500;
    font-size: 62px;
    fill: var(--white);
  }
  .product-name {
    font-family: "Kaushan Script", cursive;
    font-size: 92px;
    fill: var(--white);
  }
  .banner-shape { fill: var(--label); stroke: var(--amber); stroke-width: 3; }
  .banner-title {
    font-family: "Patua One", serif;
    font-size: 38px;
    letter-spacing: 2px;
    fill: var(--white);
  }
  .since {
    font-family: "Oswald", sans-serif;
    font-size: 21px;
    letter-spacing: 1px;
    fill: var(--white);
  }
  .website {
    font-family: "Oswald", sans-serif;
    font-size: 15px;
    fill: var(--amber);
  }
</style>
</head>
<body>
<svg class="label" viewBox="0 0 722 900" xmlns="http://www.w3.org/2000/svg">
  <rect class="label-bg" x="0" y="0" width="722" height="900"/>

  <!-- frame -->
  <rect class="frame-line" x="22" y="22" width="678" height="856" stroke-width="4" stroke-dasharray="3 3"/>
  <rect class="frame-line" x="30" y="30" width="662" height="840" stroke-width="2"/>
  <rect class="frame-line" x="38" y="38" width="646" height="824" stroke-width="1.5"/>

  <!-- corner ornaments -->
  <rect class="amber-fill" x="52" y="52" width="62" height="62" opacity="0.35" role="img" aria-label="Corner flourish ornament"/>
  <rect class="amber-fill" x="608" y="52" width="62" height="62" opacity="0.35" role="img" aria-label="Corner flourish ornament"/>
  <rect class="amber-fill" x="52" y="786" width="62" height="62" opacity="0.35" role="img" aria-label="Corner flourish ornament"/>
  <rect class="amber-fill" x="608" y="786" width="62" height="62" opacity="0.35" role="img" aria-label="Corner flourish ornament"/>

  <!-- tagline row -->
  <line class="frame-line" x1="134" y1="136" x2="284" y2="136" stroke-width="2"/>
  <line class="frame-line" x1="134" y1="172" x2="284" y2="172" stroke-width="2"/>
  <text class="tagline" x="209" y="164" text-anchor="middle">WILL BRING YOU</text>
  <rect class="amber-fill" x="288" y="98" width="146" height="108" rx="14" opacity="0.85" role="img" aria-label="Front view illustration of a 1950s classic car"/>
  <line class="frame-line" x1="438" y1="136" x2="588" y2="136" stroke-width="2"/>
  <line class="frame-line" x1="438" y1="172" x2="588" y2="172" stroke-width="2"/>
  <text class="tagline" x="513" y="164" text-anchor="middle">BACK 50 YEARS</text>

  <!-- brand name -->
  <path id="name-arc" d="M 96 380 Q 361 250 628 380" fill="none"/>
  <text class="brand-name brand-top" text-anchor="middle">
    <textPath href="#name-arc" startOffset="50%">MARBURY</textPath>
  </text>
  <rect class="amber-fill" x="160" y="390" width="60" height="24" rx="12" role="img" aria-label="Wheat sprig ornament"/>
  <text class="brand-name brand-bottom" x="361" y="428" text-anchor="middle">CREEK</text>
  <rect class="amber-fill" x="502" y="390" width="60" height="24" rx="12" role="img" aria-label="Wheat sprig ornament"/>

  <!-- number mark -->
  <rect class="amber-fill" x="236" y="478" width="70" height="56" rx="8" opacity="0.85" role="img" aria-label="Radiating line ornament"/>
  <text class="number-mark" x="361" y="524" text-anchor="middle">№1</text>
  <rect class="amber-fill" x="416" y="478" width="70" height="56" rx="8" opacity="0.85" role="img" aria-label="Radiating line ornament"/>

  <!-- product name -->
  <text class="product-name" x="361" y="648" text-anchor="middle">root beer</text>

  <!-- ribbon banner -->
  <path class="banner-shape" d="M 196 730 L 240 716 L 246 790 L 210 800 L 226 766 Z"/>
  <path class="banner-shape" d="M 526 730 L 482 716 L 476 790 L 512 800 L 496 766 Z"/>
  <path class="banner-shape" d="M 226 712 Q 361 680 496 712 L 496 758 Q 361 730 226 758 Z"/>
  <text class="banner-title" x="361" y="744" text-anchor="middle">HOMEMADE</text>
  <line class="frame-line" x1="268" y1="780" x2="288" y2="780" stroke-width="2"/>
  <text class="since" x="361" y="788" text-anchor="middle">SINCE 1965</text>
  <line class="frame-line" x1="434" y1="780" x2="454" y2="780" stroke-width="2"/>

  <!-- website -->
  <text class="website" x="361" y="835" text-anchor="middle">WWW.MARBURYCREEKDRIVEIN.EXAMPLE</text>
</svg>
</body>
</html>
```